Business Card Design

Please visit www.RobHartwell.com to acquire information for business card.

Back Side of Card:
a lifetime of experience working for you.

With over 25 years in the construction industry, well over a decade as a licensed Subcontractor / General Contractor and nearly 10 years as a licensed Realtor, I have excelled and cultivated a working knowledge of how all the pieces fit together.

Here is a link to folder.
https://files.examplestore.net/folderview?id=7Kq2XwPmR4tLvN9sBz8yHc3DfGaJ&usp=sharing

Industry/Entity Type

Construction

Contact Information for Business Card

Company: Rob Hartwell, LLC.
Address: 31872 W. Cedar Hollow Blvd. Suite 207-384
Name: Rob Hartwell
Phone: (623) 587-2914
Web: www.RobHartwell.com
Type of services offered: Architectural Design, 3D Models, Renderings & Animation - Construction Documents - Project Managment.

```html
<!DOCTYPE html>
<html lang="en">
<head>
<meta charset="utf-8">
<title>Rob Hartwell, LLC. — Business Card</title>
<link rel="stylesheet" href="https://fonts.googleapis.com/css2?family=Quicksand:wght@400;500&display=swap">
<style>
  :root {
    --backdrop: #4f5959;
    --front-blue: #2767c6;
    --front-band: #2f84ff;
    --front-type: #62a4ef;
    --back-dark: #1c1f20;
    --accent-blue: #2f84ff;
    --band-type: #0c1220;
    --contact-grey: #6d7273;
  }
  * { margin: 0; padding: 0; box-sizing: border-box; }
  html, body {
    width: 1200px; height: 741px; overflow: hidden;
    background: var(--backdrop);
    font-family: "Quicksand", sans-serif;
  }
  .stage { position: relative; width: 1200px; height: 741px; }
  .card {
    position: absolute; left: 400px; width: 408px; height: 238px; overflow: hidden;
  }
  .card-front { top: 89px; background: var(--front-blue); }
  .card-front .company-band {
    position: absolute; left: 0; top: 87px; width: 100%; height: 74px;
    background: var(--front-band);
    display: flex; align-items: center; justify-content: center;
  }
  .company-name {
    color: var(--front-type); font-size: 40px; font-weight: 400; letter-spacing: 0.5px;
    white-space: nowrap;
  }
  .card-back { top: 413px; background: var(--back-dark); }
  .person-name {
    position: absolute; left: 27px; top: 42px;
    color: var(--accent-blue); font-size: 28px; font-weight: 400; white-space: nowrap;
  }
  .services-band {
    position: absolute; left: 0; top: 96px; width: 100%; height: 70px;
    background: var(--accent-blue);
    padding: 29px 0 0 31px;
    color: var(--band-type); font-size: 12.3px; font-weight: 500; line-height: 18px;
  }
  .services-band .line-2 { padding-left: 21px; }
  .contact {
    position: absolute; color: var(--contact-grey); font-size: 12.5px;
    display: flex; align-items: center; gap: 10px; white-space: nowrap;
  }
  .contact svg { width: 12px; height: 12px; fill: var(--accent-blue); flex: none; }
  .contact-phone { left: 29px; top: 196px; }
  .contact-web { left: 199px; top: 196px; }
  .contact-address { left: 29px; top: 218px; }
</style>
</head>
<body>
<div class="stage">
  <section class="card card-front">
    <div class="company-band">
      <h1 class="company-name">Rob Hartwell, LLC.</h1>
    </div>
  </section>

  <section class="card card-back">
    <h2 class="person-name">Rob Hartwell</h2>
    <div class="services-band">
      <p class="line-1">Architectural Design, 3D Models, Renderings &amp; Animation</p>
      <p class="line-2">Construction Documents - Project Managment.</p>
    </div>
    <p class="contact contact-phone">
      <svg viewBox="0 0 24 24" aria-hidden="true"><path d="M6.6 10.8c1.4 2.8 3.8 5.1 6.6 6.6l2.2-2.2c.3-.3.7-.4 1-.2 1.1.4 2.3.6 3.6.6.6 0 1 .4 1 1V20c0 .6-.4 1-1 1C10.6 21 3 13.4 3 4c0-.6.4-1 1-1h3.5c.6 0 1 .4 1 1 0 1.3.2 2.5.6 3.6.1.3 0 .7-.2 1l-2.3 2.2z"/></svg>
      (623) 587-2914
    </p>
    <p class="contact contact-web">
      <svg viewBox="0 0 24 24" aria-hidden="true"><circle cx="12" cy="12" r="10"/><path d="M2 12h20M12 2c3 3 3 17 0 20M12 2c-3 3-3 17 0 20" stroke="#1c1f20" stroke-width="1.6" fill="none"/></svg>
      www.RobHartwell.com
    </p>
    <p class="contact contact-address">
      <svg viewBox="0 0 24 24" aria-hidden="true"><path d="M12 2C8.1 2 5 5.1 5 9c0 5.2 7 13 7 13s7-7.8 7-13c0-3.9-3.1-7-7-7zm0 9.5a2.5 2.5 0 1 1 0-5 2.5 2.5 0 0 1 0 5z"/></svg>
      31872 W. Cedar Hollow Blvd.&nbsp;&nbsp; Suite 207-384
    </p>
  </section>
</div>
</body>
</html>
```